Business Coach needs an elegant business card design

I need a business card design based around my logo for color and to look like a millionaire dollar coach. Incorporate the color of my logo with something creative and attractive that stands out. I am focused on high end companies and the card must look and feel that way.

Target Market(s)

High End Companies and Business Owners - Training People to become millionaires

Industry/Entity Type

Business

Requirements
Must have
• Front -
Logo (attached file) - Website (kolverbask.com) - Name (Darvel Kemp) Phone (412.807.5531) - Email (darvel@kolverbask.com) (My Title - Success Coach)
Back -
Slogan - Vision (see it) . Action (do it) . Transformation (be it)
Website - Learn More @ kolverbask.com

Creative High End Look!
Nice to have
Should not have
• Cheap standard look
nothing traditional

```html
<!DOCTYPE html>
<html lang="en">
<head>
<meta charset="utf-8">
<title>Darvel Kemp Coaching – Business Card</title>
<link rel="stylesheet" href="https://fonts.googleapis.com/css2?family=Cinzel:wght@400&family=Lato:wght@400;700;900&display=swap">
<style>
  :root {
    --stage: #2a2a2c;
    --navy: #1f2a55;
    --navy-light: #34427a;
    --paper: #f7f7f7;
    --paper-shade: #e6e6e6;
    --slogan-grey: #a9a9a9;
    --slogan-dark: #8c8c8c;
    --white: #ffffff;
  }
  * { box-sizing: border-box; margin: 0; padding: 0; }
  html, body { width: 1200px; height: 992px; overflow: hidden; background: var(--stage); }
  .stage {
    width: 1200px; height: 992px;
    display: flex; flex-direction: column; align-items: center; justify-content: center; gap: 48px;
  }
  .card {
    width: 780px; height: 430px; border-radius: 26px; overflow: hidden; position: relative;
    box-shadow: 0 14px 40px rgba(0,0,0,.5);
  }

  /* Back */
  .card-back { background: linear-gradient(135deg, var(--paper) 0%, var(--paper-shade) 100%); }
  .slogan {
    position: absolute; left: 70px; top: 96px;
    font-family: "Lato", sans-serif; font-weight: 700; font-size: 24px;
    letter-spacing: 2px; line-height: 56px; color: var(--slogan-grey);
    text-transform: uppercase; white-space: nowrap;
  }
  .slogan .keyword { font-weight: 900; color: var(--slogan-dark); }
  .slogan .highlight { font-weight: 900; color: var(--navy); }
  .card-back .brand { position: absolute; right: 60px; bottom: 50px; }
  .card-back .brand-dot { width: 52px; height: 52px; }
  .card-back .brand-name { font-size: 20px; }

  /* Brand placeholder: plain circle + name */
  .brand { display: flex; align-items: center; gap: 14px; }
  .brand-dot { width: 70px; height: 70px; border-radius: 50%; background: var(--navy); flex: none; }
  .brand-name {
    font-family: "Lato", sans-serif; font-weight: 700; color: var(--navy);
    font-size: 24px; white-space: nowrap;
  }

  /* Front */
  .card-front { background: var(--paper); display: flex; }
  .front-logo-area { width: 430px; display: flex; align-items: center; justify-content: center; }
  .divider { width: 40px; flex: none; }
  .info-panel {
    flex: 1; background: linear-gradient(160deg, var(--navy-light) 0%, var(--navy) 55%);
    color: var(--white); padding: 72px 0 0 54px;
  }
  .person-name { font-family: "Cinzel", serif; font-weight: 400; font-size: 30px; letter-spacing: 1px; }
  .person-title { font-family: "Lato", sans-serif; font-weight: 700; font-size: 18px; margin-top: 4px; }
  .contacts { list-style: none; margin-top: 84px; font-family: "Lato", sans-serif; font-size: 19px; }
  .contacts li { display: flex; align-items: center; gap: 12px; margin-bottom: 9px; }
  .contacts svg { width: 26px; height: 26px; flex: none; }
</style>
</head>
<body>
<main class="stage">
  <section class="card card-back" aria-label="Card back">
    <p class="slogan">
      Vision . See what you want<br>
      Action . Do what it takes<br>
      <span class="keyword">Transformation</span> . Live your <span class="highlight">Vision!</span>
    </p>
    <div class="brand">
      <div class="brand-dot"></div>
      <div class="brand-name">Darvel Kemp Coaching</div>
    </div>
  </section>

  <section class="card card-front" aria-label="Card front">
    <div class="front-logo-area">
      <div class="brand">
        <div class="brand-dot"></div>
        <div class="brand-name">Darvel Kemp Coaching</div>
      </div>
    </div>
    <svg class="divider" viewBox="0 0 40 430" preserveAspectRatio="none" aria-hidden="true">
      <rect x="4" y="0" width="4" height="430" fill="var(--navy)"/>
      <rect x="14" y="0" width="4" height="430" fill="var(--navy)"/>
      <rect x="24" y="0" width="4" height="430" fill="var(--navy)"/>
    </svg>
    <div class="info-panel">
      <h1 class="person-name">DARVEL KEMP</h1>
      <p class="person-title">Success Coach</p>
      <ul class="contacts">
        <li>
          <svg viewBox="0 0 26 26" aria-hidden="true"><rect x="1" y="1" width="24" height="24" rx="4" fill="var(--white)"/><path d="M8 7c-1 1-1 3 1 6s4 5 6 6c1 .4 2 0 3-1l-2-3-2 1c-1-.5-3-2.5-3.5-3.5l1-2-3-3.5z" fill="var(--navy)"/></svg>
          412.807.5531
        </li>
        <li>
          <svg viewBox="0 0 26 26" aria-hidden="true"><rect x="1" y="1" width="24" height="24" rx="4" fill="var(--white)"/><rect x="5" y="8" width="16" height="11" fill="none" stroke="var(--navy)" stroke-width="1.6"/><path d="M5 8l8 6 8-6" fill="none" stroke="var(--navy)" stroke-width="1.6"/></svg>
          darvel@kolverbask.com
        </li>
        <li>
          <svg viewBox="0 0 26 26" aria-hidden="true"><rect x="1" y="1" width="24" height="24" rx="4" fill="var(--white)"/><circle cx="13" cy="13" r="7" fill="none" stroke="var(--navy)" stroke-width="1.5"/><ellipse cx="13" cy="13" rx="3" ry="7" fill="none" stroke="var(--navy)" stroke-width="1.3"/><path d="M6 13h14" stroke="var(--navy)" stroke-width="1.3"/></svg>
          www.kolverbask.com
        </li>
      </ul>
    </div>
  </section>
</main>
</body>
</html>
```